Marketing One-Sheet for Security Deposit Claim Notice

I need a one-sheet flyer formatted for email distribution — optimized as a JPEG/PNG that I can insert into Constant Contact or Outlook. I do not want to attach it to an email, but insert it in the email we send out. I would like it to look professional but engaging. Some images would be good, but want to make sure it reads well if images do not load for the recipients. The text is in the attached Word document, but I am open to changes/ideas that may be better for marketing purposes. I included the URLs for some of the links I would like in the one-sheet that is clickable. The logo for the business is being uploaded on the Word document. Proposed text is also uploaded in a Word document. Thank you.

Target Market(s)

Landlords, Real Estate Agents, Property Managers

Industry/Entity Type

Legal

Requirements
Must have
• Professional but appealing design. The One-sheet is going to be placed in the body of emails, not as an attachment.
Nice to have
• Include our logo for the business and the web links please.
Should not have
• Images can be ok, but it needs to look right if images do not download from the email sent out.

```html
<!DOCTYPE html>
<html lang="en">
<head>
<meta charset="utf-8">
<title>Security Deposit Claim Notice</title>
<link href="https://fonts.googleapis.com/css2?family=Playfair+Display:wght@400;700&family=Source+Serif+4:wght@400;600&display=swap" rel="stylesheet">
<style>
:root{
  --red:#e52f32;
  --deep-red:#c8101e;
  --charcoal:#333333;
  --panel:#f3f3f3;
  --ink:#1d1d1d;
  --body:#3a3a3a;
  --white:#ffffff;
  --dark-bg:#2a2626;
}
*{margin:0;padding:0;box-sizing:border-box}
html,body{width:1200px;height:2794px;overflow:hidden;background:var(--white)}
body{position:relative;font-family:"Source Serif 4",Georgia,serif;color:var(--body)}
.abs{position:absolute}
.display{font-family:"Playfair Display",Georgia,serif}

.topbar{left:0;top:0;width:1200px;height:135px;background:var(--panel)}
.brand{left:0;top:0;width:1200px;height:135px;display:flex;flex-direction:column;align-items:center;justify-content:center;gap:4px}
.brand-name{font-family:"Playfair Display",Georgia,serif;font-size:30px;color:var(--deep-red);letter-spacing:1px;display:flex;align-items:center;gap:10px}
.brand-name .dot{width:16px;height:16px;background:var(--deep-red)}
.brand-sub{font-size:13px;color:var(--deep-red);font-weight:600}

.hero-panel{left:0;top:135px;width:588px;height:586px;background:linear-gradient(135deg,#d4101f,#b50f1c)}
.hero-photo{left:588px;top:135px;width:612px;height:586px;background:linear-gradient(150deg,#6a3a33 0%,#4a2a26 45%,#8a6a3a 70%,#3a2320 100%)}
.hero-kicker{left:68px;top:290px;width:480px;font-size:36px;line-height:43px;color:var(--white)}
.hero-title{left:68px;top:392px;width:500px;font-size:54px;line-height:57px;font-weight:700;color:var(--white)}

.benefits-title{left:0;top:796px;width:1200px;text-align:center;font-size:45px;color:var(--red);font-weight:700}
.benefit{top:894px;width:321px;height:247px;display:flex;flex-direction:column;align-items:center;justify-content:flex-end;padding-bottom:26px;color:var(--white);text-align:center;font-family:"Playfair Display",Georgia,serif;font-weight:700;font-size:24px;line-height:29px}
.benefit svg{margin-bottom:24px}
.benefit.dark{background:var(--charcoal)}
.benefit.accent{background:var(--red)}

.dark-section{left:33px;top:1572px;width:1134px;height:1038px;background:linear-gradient(160deg,#4a2f2e 0%,var(--dark-bg) 45%,#1f1e1e 100%)}
.offer-card{left:66px;top:1243px;width:1066px;height:579px;background:var(--panel);border:2px solid #e8868a}
.offer-photo{left:106px;top:1302px;width:414px;height:460px;background:linear-gradient(160deg,#7a4a2a 0%,#a0602e 35%,#c98a6a 60%,#e8ddd0 100%)}
.offer-title{left:564px;top:1290px;width:540px;font-size:45px;line-height:54px;color:var(--red);font-weight:700}
.offer-fee{left:564px;top:1430px;font-size:30px;color:var(--ink);font-weight:600}
.offer-lead{left:564px;top:1488px;width:540px;font-size:22px;line-height:28px}
.offer-list{left:564px;top:1568px;width:520px;list-style:none;font-size:22px;line-height:28px;color:#4a4a4a}
.offer-list li{position:relative;padding-left:44px;margin-bottom:21px}
.offer-list li::before{content:"»";position:absolute;left:2px;top:-6px;font-size:34px;color:var(--deep-red);font-weight:700}

.note{left:120px;top:1910px;width:960px;text-align:center;font-size:22px;line-height:33px;color:var(--white)}
.commercial{left:0;top:2046px;width:1200px;text-align:center;font-size:30px;color:var(--white);font-weight:700;text-decoration:underline}
.rule{left:112px;top:2187px;width:976px;height:1px;background:#9a9a9a}
.rule-strong{left:476px;top:2183px;width:248px;height:8px;background:var(--white)}

.contact-title{left:81px;top:2288px;font-size:48px;color:var(--white);font-weight:700}
.contact-sub{left:81px;top:2358px;width:460px;font-size:23px;line-height:33px;color:#e6e6e6}
.contact-list{right:80px;top:2317px;list-style:none;font-size:26px;color:var(--white)}
.contact-list li{display:flex;align-items:center;gap:18px;height:42px;white-space:nowrap}

.ribbon{left:66px;top:2520px;width:1066px;height:177px}
.ribbon-text{left:66px;top:2566px;width:1066px;text-align:center;font-size:25px;line-height:41px;color:var(--white)}
.ribbon-text a{color:var(--white)}
.copyright{left:0;top:2738px;width:1200px;text-align:center;font-size:17px;color:var(--body)}
</style>
</head>
<body>
<div class="abs topbar"></div>
<div class="abs brand">
  <div class="brand-name"><span>Tenancy Counsel Group</span><span class="dot"></span></div>
  <div class="brand-sub">TenancyCounselGroup.com · 1(888) 555-0147</div>
</div>

<div class="abs hero-panel"></div>
<div class="abs hero-photo" role="img" aria-label="Photo of a landlord-tenant law book with a wooden gavel"></div>
<p class="abs hero-kicker display">SECURITY DEPOSIT CLAIM NOTICE</p>
<h1 class="abs hero-title display">Keep the Tenant’s Security Deposit — The Right Way</h1>

<h2 class="abs benefits-title display">KEY BENEFITS</h2>
<div class="abs benefit dark" style="left:66px">
  <svg width="112" height="112" viewBox="0 0 112 112" fill="none" stroke="#fff" stroke-width="7" stroke-linejoin="round"><path d="M8 52 56 10l48 42"/><path d="M22 42v60h68V42"/><rect x="16" y="58" width="80" height="30" fill="#333" stroke-width="5"/><text x="56" y="82" text-anchor="middle" font-family="Georgia,serif" font-size="24" font-weight="700" fill="#fff" stroke="none">RENT</text></svg>
  <span>Cover Unpaid<br>Rent</span>
</div>
<div class="abs benefit accent" style="left:441px">
  <svg width="112" height="112" viewBox="0 0 112 112" fill="none" stroke="#fff" stroke-width="7" stroke-linejoin="round"><rect x="8" y="14" width="96" height="60" rx="6"/><circle cx="56" cy="44" r="16"/><path d="M30 74v26h40"/></svg>
  <span>Apply Funds To Legal<br>Fees &amp; Costs</span>
</div>
<div class="abs benefit dark" style="left:814px">
  <svg width="112" height="112" viewBox="0 0 112 112"><path d="M56 8 4 54h14v50h76V54h14z" fill="#fff"/><path d="M60 20 48 50l14 18-10 36" stroke="#333" stroke-width="6" fill="none"/><rect x="72" y="62" width="12" height="12" fill="#333"/></svg>
  <span>Charge Against<br>Property Damages</span>
</div>

<div class="abs dark-section" role="img" aria-label="Dim photo of a house porch at dusk behind the text"></div>
<div class="abs offer-card"></div>
<div class="abs offer-photo" role="img" aria-label="Photo of a hand signing a legal document in front of law books"></div>
<h2 class="abs offer-title display">We Prepare Security Deposit Claim Notices</h2>
<p class="abs offer-fee">Flat Legal Fee: $350 (Residential)</p>
<p class="abs offer-lead">If the Security Deposit Claim is not made correctly and on time, then:</p>
<ul class="abs offer-list">
  <li>Tenant is automatically entitled to their full deposit back</li>
  <li>No claim against the deposit can be made</li>
  <li>Tenant can sue and recover the deposit and thousands in legal fees</li>
</ul>

<p class="abs note">There are lawyers that specialize in representing tenants and go after landlords that do not make a proper claim against the security deposit. They sue and win their cases and get thousands of dollars in legal fees against Landlords, even if the tenant owes unpaid rent.</p>
<p class="abs commercial display">Commercial Properties: Flat legal fee $450</p>
<div class="abs rule"></div>
<div class="abs rule-strong"></div>

<h2 class="abs contact-title display">Contact Us</h2>
<p class="abs contact-sub">Hire Us to prepare and serve to the tenant the security deposit claim</p>
<ul class="abs contact-list">
  <li><svg width="26" height="26" viewBox="0 0 24 24" fill="none" stroke="#fff" stroke-width="2"><circle cx="12" cy="12" r="10"/><path d="M2 12h20M12 2c3 3 3 17 0 20M12 2c-3 3-3 17 0 20"/></svg>TenancyCounselGroup.com</li>
  <li><svg width="26" height="26" viewBox="0 0 24 24" fill="#fff"><path d="M6.6 10.8a15 15 0 0 0 6.6 6.6l2.2-2.2a1 1 0 0 1 1-.25 11.4 11.4 0 0 0 3.6.57 1 1 0 0 1 1 1V20a1 1 0 0 1-1 1A17 17 0 0 1 3 4a1 1 0 0 1 1-1h3.5a1 1 0 0 1 1 1c0 1.250.2 2.45.57 3.6a1 1 0 0 1-.25 1z"/></svg>1888-555-0147</li>
</ul>

<svg class="abs ribbon" viewBox="0 0 1066 177" aria-hidden="true">
  <polygon points="0,0 1066,0 1048,88 1066,177 0,177 18,88" fill="#e52f32"/>
  <polygon points="14,12 1052,12 1036,88 1052,165 14,165 30,88" fill="none" stroke="#fff" stroke-width="2"/>
</svg>
<p class="abs ribbon-text">More information: <a href="https://tenancycounselgroup.com/keeping-security-deposits/">https://tenancycounselgroup.com/keeping-security-deposits/</a><br>Request our hiring documents: <a href="https://tenancycounselgroup.com/hire-lawyer/">https://tenancycounselgroup.com/hire-lawyer/</a></p>

<p class="abs copyright">Copyright © 2025 Tenancy Counsel Group. All rights reserved.</p>
</body>
</html>
```